FACIAL COSMETICS BUSINESS CARD

WE ARE A DENTAL PRACTICE BUT ARE OPENING UP A BRANCH FOR FACILA COSMETICS, LIKE BOTOX, FILLERS, PEELS, ETC. MAEVE AND ISOLDA WILL BE RUNNING THAT PART OF THE BUSINESS.
OUR CURRENT CARD IS ATTACHED AND OUR LOGO IT ATTACHED TOO. THE LOGO HAS ON IT OVEN DENTAL, I WOULD LIKE IT TO SAY OVEN COSMETICS, THE PHONE NUMBERS ON IT HAS TO BE REPLACED BY THE ONES I GAVE PREVIOUSLY AND THE WEB ADDRESS HAS TO BE DELETED, THE OTHER SIDE OF THE CARD HAS A MAP WHICH HAS TO BE DELETED, ADD TWO DATE-TIME LINES, I LIKE THE CARDS TO BE SIMPLE AND CLEAN, SIZE HAS TO BE NO LARGER THAN 5CMx8.5CM.
THE CARD HAS TO BE MATTE, I HATE GLOSSY, ABLE TO BE WRITTEN ON BOTH SIDES

Updates
I HAVE ATTACHED THE FILES, THEY CONSIST OF OUR CURRENT LOGO IN A FEW FORMS AND OUR BUSINESS CARD FOR THE DENTAL BRANCH, PLEASE COPY THE CURRENT DESIGN BUT ADDING THE REQUESTED CHANGES

Industry/Entity Type
Business
Contact Information for Business Card
OVEN COSMETICS
MAEVE : 0438 572 913
ISOLDA : 0429 638 207
SUITE 8 COLWOOD PARK ARCADE
74-86 HALBERT STREET
COLWOOD PARK NSW 2284
Logo Text
OVEN COSMETICS
Look and feel

```html
<!DOCTYPE html>
<html lang="en">
<head>
<meta charset="utf-8">
<title>Oven Cosmetics – Business Card</title>
<link rel="stylesheet" href="https://fonts.googleapis.com/css2?family=Michroma&family=Tinos&family=Open+Sans:wght@600&display=swap">
<style>
  :root {
    --backdrop: #808080;
    --card: #fbfbfb;
    --card-shade: #f3f3f3;
    --green: #43ac48;
    --ink: #1d1d1d;
  }
  * { box-sizing: border-box; margin: 0; padding: 0; }
  html, body {
    width: 1200px;
    height: 900px;
    overflow: hidden;
    background: var(--backdrop);
  }
  .canvas { position: relative; width: 1200px; height: 900px; }
  .card {
    position: absolute;
    width: 415px;
    overflow: hidden;
    background: linear-gradient(90deg, var(--card-shade), var(--card) 35%, #ffffff);
  }
  .card--front { left: 101px; top: 93px; height: 704px; }
  .card--back  { left: 679px; top: 93px; height: 706px; }
  .card__band { position: absolute; left: 0; top: 0; width: 415px; height: 100%; }

  .brand {
    position: absolute;
    left: 0; width: 100%;
    text-align: center;
    font-family: "Michroma", sans-serif;
    color: var(--ink);
    line-height: 1;
    white-space: nowrap;
  }
  .card--front .brand { top: 160px; font-size: 24px; letter-spacing: 2px; }
  .card--back .brand { top: 92px; font-size: 15px; letter-spacing: 1.5px; }

  .title {
    position: absolute;
    left: 0; width: 100%;
    text-align: center;
    font-family: "Michroma", sans-serif;
    font-weight: 400;
    color: var(--ink);
    line-height: 1;
  }
  .title__line { display: block; }
  .title__line--main { font-size: 24px; letter-spacing: 6px; }
  .title__line--sub { font-size: 22px; letter-spacing: 5px; margin-top: 20px; }
  .card--front .title { top: 340px; }

  .contacts {
    position: absolute;
    left: 43px; top: 452px;
    font-family: "Tinos", serif;
    font-size: 28px;
    letter-spacing: 1.4px;
    color: var(--ink);
    list-style: none;
  }
  .contacts__item { display: flex; height: 44px; white-space: nowrap; }
  .contacts__name { width: 134px; }

  .address {
    position: absolute;
    left: 0; width: 100%; top: 618px;
    text-align: center;
    font-family: "Michroma", sans-serif;
    font-size: 12px;
    letter-spacing: 2.4px;
    line-height: 21px;
    color: var(--ink);
    font-style: normal;
    white-space: nowrap;
  }

  .appointments {
    position: absolute;
    left: 40px; top: 258px;
    font-family: "Open Sans", sans-serif;
    font-weight: 600;
    font-size: 18px;
    color: var(--ink);
    list-style: none;
  }
  .appointments__field { height: 54px; letter-spacing: 0.6px; white-space: nowrap; }
  .appointments__field--gap { margin-top: 58px; }
  .appointments__dots { color: var(--green); letter-spacing: 1px; }
</style>
</head>
<body>
<main class="canvas">

  <section class="card card--front" aria-label="Card front">
    <svg class="card__band" viewBox="0 0 415 704" aria-hidden="true">
      <path d="M0 279 Q208 346 415 288 L415 492 Q208 662 0 492 Z" fill="var(--green)"/>
    </svg>
    <p class="brand">OVEN COSMETICS</p>
    <h1 class="title">
      <span class="title__line title__line--main">OVEN</span>
      <span class="title__line title__line--sub">COSMETICS</span>
    </h1>
    <ul class="contacts">
      <li class="contacts__item"><span class="contacts__name">MAEVE</span><span>: 0438 572 913</span></li>
      <li class="contacts__item"><span class="contacts__name">ISOLDA</span><span>: 0429 638 207</span></li>
    </ul>
    <address class="address">
      SUITE 8, COLWOOD PARK ARCADE,<br>
      74-86 HALBERT STREET,<br>
      COLWOOD PARK NSW 2284
    </address>
  </section>

  <section class="card card--back" aria-label="Card back">
    <svg class="card__band" viewBox="0 0 415 706" aria-hidden="true">
      <path d="M0 624 Q208 695 415 634 L415 706 L0 706 Z" fill="var(--green)"/>
    </svg>
    <p class="brand">OVEN COSMETICS</p>
    <ul class="appointments">
      <li class="appointments__field">Date : <span class="appointments__dots">......................</span></li>
      <li class="appointments__field">Time : <span class="appointments__dots">......................</span></li>
      <li class="appointments__field appointments__field--gap">Date : <span class="appointments__dots">......................</span></li>
      <li class="appointments__field">Time : <span class="appointments__dots">......................</span></li>
    </ul>
  </section>

</main>
</body>
</html>
```